Gourmet butcher shop needs a business card design

We need a business card design for an upmarket butcher shop in Brisbane, Queensland Australia. We would prefer the card to be printed on a brown craft paper business card and would consider the use of raised print on the card. The card needs to make space for the usual information: ABN, address, telephone, facebook page. I stress it is a gourmet shop in a wealthy suburb. Thanks

Industry/Entity Type

Business

Contact Information for Business Card

Address Shop 2, Wendmoor Arcade, 417 Purlow Street, Wendmoor
Telephone 07 5914 3027
A.B.N. 73 508 914 226
Facebook www.fakebooksite.example/wendmoorarcadecuts

Requirements
Should not have
• No need for a person's name or title

```html
<!DOCTYPE html>
<html lang="en">
<head>
<meta charset="utf-8">
<title>Wendmoor Arcade Meats – Business Card</title>
<link rel="stylesheet" href="https://fonts.googleapis.com/css2?family=Open+Sans:wght@400;600&display=swap">
<style>
  :root {
    --backdrop: #e9e6e1;
    --card: #ffffff;
    --brand-red: #d42a47;
    --ink: #222222;
    --arc-ink: #2d2d2d;
    --rule: #3a3a3a;
  }
  * { box-sizing: border-box; margin: 0; padding: 0; }
  html, body { width: 1200px; height: 892px; overflow: hidden; }
  body {
    background: var(--backdrop);
    font-family: "Open Sans", Arial, sans-serif;
    color: var(--ink);
    display: flex;
    align-items: center;
    justify-content: center;
    gap: 40px;
  }
  .card {
    position: relative;
    width: 560px;
    height: 320px;
    background: var(--card);
    box-shadow: 0 6px 18px rgba(0,0,0,0.18);
    overflow: hidden;
  }
  .card__corner { position: absolute; inset: 0; width: 560px; height: 320px; }

  .brand {
    position: absolute;
    display: flex;
    flex-direction: column;
    align-items: center;
    gap: 8px;
  }
  .brand__rule { width: 100%; height: 1px; background: var(--rule); }
  .brand__name {
    font-weight: 600;
    color: var(--brand-red);
    text-transform: uppercase;
    text-align: center;
    line-height: 1.1;
    letter-spacing: 1px;
  }

  .card--front .brand { left: 34px; top: 36px; width: 200px; }
  .card--front .brand__name { font-size: 24px; }

  .contact {
    position: absolute;
    left: 34px; top: 150px;
    list-style: none;
    display: flex;
    flex-direction: column;
    gap: 8px;
    font-size: 14px;
    line-height: 1.35;
  }
  .contact__item { display: flex; align-items: flex-start; gap: 10px; }
  .contact__icon { width: 16px; height: 16px; flex: none; margin-top: 2px; }

  .abn-line {
    position: absolute;
    left: 300px; right: 0; top: 286px;
    display: flex; align-items: center; gap: 10px;
    font-size: 14px;
  }
  .abn-line__rule { flex: 1; height: 1px; background: var(--rule); }
  .abn-line__rule--short { flex: 0 0 18px; }

  .card--back .brand { left: 50%; top: 50%; transform: translate(-50%, -50%); width: 320px; gap: 14px; }
  .card--back .brand__name { font-size: 38px; }
</style>
</head>
<body>

  <section class="card card--front" aria-label="Business card front">
    <svg class="card__corner" viewBox="0 0 560 320" aria-hidden="true">
      <path d="M330 0 A250 210 0 0 0 560 200 L560 0 Z" fill="var(--brand-red)"/>
      <path d="M330 0 A250 210 0 0 0 560 200" fill="none" stroke="var(--arc-ink)" stroke-width="4"/>
    </svg>

    <div class="brand">
      <span class="brand__rule"></span>
      <span class="brand__name">Wendmoor Arcade Meats</span>
      <span class="brand__rule"></span>
    </div>

    <ul class="contact">
      <li class="contact__item">
        <svg class="contact__icon" viewBox="0 0 16 16" aria-hidden="true">
          <rect width="16" height="16" fill="var(--brand-red)"/>
          <path d="M5 3.5 L7 5.5 L6 7 Q7 9 9 10 L10.5 9 L12.5 11 L11 12.5 Q6 12 3.5 5 Z" fill="#fff"/>
        </svg>
        <span>07 5914 3027</span>
      </li>
      <li class="contact__item">
        <svg class="contact__icon" viewBox="0 0 16 16" aria-hidden="true">
          <rect width="16" height="16" fill="var(--brand-red)"/>
          <circle cx="8" cy="8" r="4.5" fill="none" stroke="#fff" stroke-width="1.2"/>
          <path d="M3.5 8 H12.5 M8 3.5 Q5.5 8 8 12.5 M8 3.5 Q10.5 8 8 12.5" fill="none" stroke="#fff" stroke-width="1"/>
        </svg>
        <span>www.fakebooksite.example/wendmoorarcadecuts</span>
      </li>
      <li class="contact__item">
        <svg class="contact__icon" viewBox="0 0 16 16" aria-hidden="true">
          <rect width="16" height="16" fill="var(--brand-red)"/>
          <path d="M8 13 L4.8 8 A3.6 3.6 0 1 1 11.2 8 Z" fill="#fff"/>
          <circle cx="8" cy="6.3" r="1.3" fill="var(--brand-red)"/>
        </svg>
        <span>Shop 2, Wendmoor Arcade,<br>417 Purlow Street, Wendmoor</span>
      </li>
    </ul>

    <div class="abn-line">
      <span class="abn-line__rule abn-line__rule--short"></span>
      <span>ABN 73 508 914 226</span>
      <span class="abn-line__rule"></span>
    </div>
  </section>

  <section class="card card--back" aria-label="Business card back">
    <div class="brand">
      <span class="brand__rule"></span>
      <span class="brand__name">Wendmoor Arcade Meats</span>
      <span class="brand__rule"></span>
    </div>
  </section>

</body>
</html>
```